Varnel Solutions requires a new business card.

We are an online professional tool store.

Target Market(s)

We target the professional technician.

Industry/Entity Type

Business

Contact Information for Business Card

VarnelSolutions.com.au

sales@varnelsolutions.com

Requirements
Must have
• Needs to look commercial and professional
Should not have
• No Australian Colors, maps or shapes.
• No Shapes of Tools

```html
<!DOCTYPE html>
<html lang="en">
<head>
<meta charset="utf-8">
<title>Varnel Solutions – Business Card</title>
<link rel="stylesheet" href="https://fonts.googleapis.com/css2?family=Open+Sans:wght@400;600;700&display=swap">
<style>
  :root {
    --backdrop: #4a423e;
    --card: #151517;
    --card-edge: #222226;
    --brand-blue: #2b3fd0;
    --brand-cyan: #1f8fc6;
    --text-light: #f2f2f2;
    --text-muted: #9a9aa0;
    --divider: #8a8a90;
  }
  * { box-sizing: border-box; margin: 0; padding: 0; }
  html, body { width: 1200px; height: 864px; overflow: hidden; }
  body {
    background: var(--backdrop);
    font-family: "Open Sans", Arial, sans-serif;
  }
  .canvas { position: relative; width: 1200px; height: 864px; }

  .card {
    position: absolute;
    width: 540px;
    height: 309px;
    background: var(--card);
    border: 1px solid var(--card-edge);
    border-radius: 4px;
    box-shadow: 0 14px 30px rgba(0,0,0,.45);
  }

  /* Front */
  .card-front { left: 60px; top: 90px; }
  .card-front .brand {
    position: absolute; left: 70px; top: 95px;
    display: flex; align-items: center; gap: 14px;
  }
  .brand-dot {
    width: 34px; height: 34px; border-radius: 50%;
    background: var(--brand-cyan);
    flex: none;
  }
  .brand-name {
    font-weight: 700; font-size: 34px; letter-spacing: .5px;
    color: var(--brand-blue);
    white-space: nowrap;
  }
  .card-front .website {
    position: absolute; left: 70px; top: 190px;
    font-size: 14px; letter-spacing: 3px; color: var(--text-muted);
  }

  /* Back */
  .card-back { left: 600px; top: 440px; }
  .card-back .brand {
    position: absolute; left: 16px; top: 136px;
    width: 230px;
    display: flex; align-items: center; justify-content: center; gap: 8px;
  }
  .card-back .brand-dot { width: 22px; height: 22px; }
  .card-back .brand-name { font-size: 19px; letter-spacing: .3px; }
  .divider {
    position: absolute; left: 262px; top: 36px;
    width: 1px; height: 236px; background: var(--divider);
  }
  .details {
    position: absolute; left: 284px; top: 44px;
    color: var(--text-light);
  }
  .person-name {
    font-weight: 700; font-size: 19px; letter-spacing: .5px;
    color: var(--brand-blue); text-transform: uppercase;
  }
  .person-role {
    font-size: 13px; color: var(--brand-cyan);
    text-transform: uppercase; margin-bottom: 8px;
  }
  .address { font-size: 14px; line-height: 1.3; margin-bottom: 6px; }
  .contact-list { list-style: none; font-size: 14px; line-height: 1.45; }
  .contact-list li { display: flex; align-items: center; gap: 10px; }
  .contact-list svg { width: 12px; height: 12px; fill: var(--brand-blue); flex: none; }
</style>
</head>
<body>
<main class="canvas">

  <section class="card card-front" aria-label="Card front">
    <div class="brand">
      <span class="brand-dot"></span>
      <span class="brand-name">Varnel Solutions</span>
    </div>
    <p class="website">www.VarnelSolutions.com.au</p>
  </section>

  <section class="card card-back" aria-label="Card back">
    <div class="brand">
      <span class="brand-dot"></span>
      <span class="brand-name">Varnel Solutions</span>
    </div>
    <span class="divider"></span>
    <div class="details">
      <p class="person-name">Mara Kellen</p>
      <p class="person-role">President</p>
      <p class="address">2170 Harborview Lane<br>Lakemont, NY 11520</p>
      <ul class="contact-list">
        <li>
          <svg viewBox="0 0 12 12" aria-hidden="true"><path d="M2.5 0.5l2 2.5-1.2 1.4c.8 1.7 2 2.9 3.3 3.5L8 6.6l2.5 2-1.2 2.6C4.8 11 1 7.2 0.7 2.2z"/></svg>
          555 0142 7730
        </li>
        <li>
          <svg viewBox="0 0 12 12" aria-hidden="true"><path d="M3 0h6v12H3zM4 1.2v8.3h4V1.2z"/></svg>
          555 0198 4416
        </li>
        <li>
          <svg viewBox="0 0 12 12" aria-hidden="true"><path d="M3 0h5v3H3zM1 4h10v6H1zM3 10h6v2H3z"/></svg>
          555 0163 2089
        </li>
        <li>
          <svg viewBox="0 0 12 12" aria-hidden="true"><path d="M0 2h12v8H0zM1 3l5 3.5L11 3v-.2H1z"/></svg>
          sales@varnelsolutions.com
        </li>
        <li>
          <svg viewBox="0 0 12 12" aria-hidden="true"><circle cx="6" cy="6" r="6"/></svg>
          VarnelSolutions.com.au
        </li>
      </ul>
    </div>
  </section>

</main>
</body>
</html>
```